Velmora Diagnostics Website

Project Description – Velmora Website Design
We need a clean, modern, and professional website for Velmora Diagnostics, a Ashgrove Hollis University of Dunmere spin-out focused on early cancer detection. Our first product, GlandSURE™, is a urine-based risk assessment test for pancreatic cancer, supported by strong clinical validation and partnerships with leading hospitals.

The site should:

Communicate trust, innovation, and clinical credibility.
Feature a clear value proposition on the home page with strong calls to action for investors, clinicians, and partners.
Showcase our technology, science, and clinical evidence in a way that is accessible but authoritative.
Highlight our university heritage, team, and collaborators.
Include sections for products/services, news/press, and contact forms.
Be fully responsive, WordPress compatible, SEO-friendly, and WCAG 2.1 AA accessible.

We want a minimalist, elegant design with subtle animations, strong visuals (e.g., science/biotech imagery), and a clear structure for future growth.
Deliverables should include editable design files (Figma/Sketch/Adobe XD) and a style guide.

```html
<!DOCTYPE html>
<html lang="en">
<head>
<meta charset="utf-8">
<title>Velmora DX – Early Cancer Detection</title>
<link rel="stylesheet" href="https://fonts.googleapis.com/css2?family=Open+Sans:wght@300;400;500;600;700;800&display=swap">
<style>
:root{
  --blue:#2f7fd0;
  --blue-deep:#1d5fae;
  --blue-light:#5fc3ec;
  --sky:#e9f4fc;
  --yellow:#f5c838;
  --ink:#151b24;
  --muted:#6d7580;
  --white:#ffffff;
  --line:#d9dee5;
}
*{box-sizing:border-box;margin:0;padding:0}
html,body{width:1200px;height:4528px;overflow:hidden;background:var(--white)}
body{font-family:"Open Sans",sans-serif;color:var(--ink);position:relative}
a{text-decoration:none;color:inherit}
.abs{position:absolute}
.photo{position:absolute;overflow:hidden}
.btn{position:absolute;display:flex;align-items:center;justify-content:center;border:4px solid var(--yellow);border-radius:30px;background:var(--white);font-size:12px;font-weight:700;color:var(--ink);letter-spacing:.2px;text-decoration:none}
.brand{font-weight:600;color:var(--blue);display:flex;align-items:center;gap:10px}
.brand .dot{width:14px;height:14px;border-radius:50%;background:var(--yellow)}

/* header */
.site-header{position:absolute;left:0;top:0;width:1200px;height:81px;background:var(--white);border-radius:0 0 18px 18px;z-index:3}
.site-header .brand{position:absolute;left:155px;top:22px;font-size:24px;letter-spacing:1px}
.nav a{position:absolute;top:32px;font-size:12px;color:var(--ink)}
.contact-btn{left:917px;top:18px;width:132px;height:45px;border-color:var(--blue)}

/* hero */
.hero{position:absolute;left:0;top:70px;width:1200px;height:665px;background:radial-gradient(circle at 78% 38%,#5aa6e6 0%,#2e78cb 40%,#1a4f9c 100%)}
.hero h1{position:absolute;left:153px;top:160px;font-size:72px;font-weight:800;color:var(--white);letter-spacing:2px}
.hero .sub{position:absolute;left:153px;font-size:42px;font-weight:300;color:var(--white);letter-spacing:1px}
.ux-label{position:absolute;left:838px;top:410px;font-size:18px;font-weight:700;color:var(--white);line-height:22px}
.play{position:absolute;width:34px;height:34px;border-radius:50%;background:var(--white);display:flex;align-items:center;justify-content:center}
.hero-dot{position:absolute;left:154px;top:574px;width:30px;height:30px;border-radius:50%;background:var(--yellow)}
.hero-note{position:absolute;left:218px;top:570px;font-size:12.5px;color:var(--white);line-height:20px}

/* sections */
.section-title{position:absolute;left:0;width:1200px;text-align:center;font-size:30px;font-weight:500;letter-spacing:.3px}
.edge-card{position:absolute;top:929px;width:213px;height:197px;border:2px solid var(--ink);border-radius:14px;background:var(--white);text-align:center}
.edge-card.active{background:var(--blue-light);border-color:var(--blue-light)}
.edge-card svg{position:absolute;left:56px;top:20px}
.edge-card p{position:absolute;left:0;right:0;bottom:22px;font-size:15.5px;line-height:19px}

.about h2{position:absolute;left:610px;font-size:30px;font-weight:500;line-height:50px}
.about p{position:absolute;left:610px;width:390px;font-size:12.3px;line-height:18px;color:#333}

.test{position:absolute;left:0;top:1711px;width:1200px;height:573px;background:linear-gradient(90deg,#2f80cf 0%,#3a86c9 45%,#1d4d86 100%)}
.test h2{position:absolute;left:151px;top:88px;font-size:29px;font-weight:500;color:var(--white)}
.test .item{position:absolute;left:151px;font-size:16px;color:var(--white)}
.test .item b{font-weight:400;font-size:19px;margin-right:4px}
.test .note{position:absolute;left:172px;font-size:12.5px;color:#d6e6f6}

.evidence-card{position:absolute;top:2477px;width:212px;height:357px;background:var(--white);border-radius:10px;box-shadow:0 4px 14px rgba(0,0,0,.12);text-align:center}
.evidence-card.active{background:var(--blue-light)}
.evidence-card .photo{left:6px;top:6px;width:200px;height:180px;border-radius:6px}
.badge{position:absolute;width:46px;height:46px;border-radius:50%;background:var(--yellow);border:3px solid var(--white)}
.evidence-card .badge{left:83px;top:150px}
.evidence-card h3{position:absolute;left:0;right:0;top:216px;font-size:15.5px;font-weight:500;line-height:21px}
.evidence-card .desc{position:absolute;left:10px;right:10px;top:266px;font-size:9.5px;line-height:13px;color:var(--muted)}
.evidence-card.active .desc{color:#1d3650}
.evidence-card .more{position:absolute;left:0;right:0;top:324px;font-size:11px;font-weight:700}

.clarity h2{position:absolute;left:155px;top:3012px;font-size:32px;font-weight:500;line-height:47px}
.acc{position:absolute;left:155px;width:434px;border-radius:8px;font-size:14.5px;font-weight:500;padding-left:22px;display:flex;align-items:center;justify-content:space-between;padding-right:18px;box-shadow:0 3px 10px rgba(0,0,0,.1);background:var(--white)}
.acc span{font-size:20px;font-weight:600}
.acc.open{background:var(--blue-light)}
.acc-body{position:absolute;left:155px;top:3196px;width:434px;height:114px;border:2px solid var(--blue-deep);border-radius:8px;padding:12px 22px;font-size:12.3px;line-height:23px}

.news-card{position:absolute;top:3640px;width:293px;height:377px;background:var(--white);border-radius:10px;box-shadow:0 4px 14px rgba(0,0,0,.13)}
.news-card .photo{left:14px;top:15px;width:265px;height:175px;border-radius:4px}
.news-card h3{position:absolute;left:14px;top:216px;font-size:15px;font-weight:500}
.news-card .lead{position:absolute;left:14px;top:250px;width:230px;font-size:12px;line-height:18px}
.news-card hr{position:absolute;left:0;right:0;top:299px;border:0;border-top:2px solid #555}
.news-card .author{position:absolute;left:14px;top:318px;display:flex;align-items:center;gap:10px;font-size:12px;font-weight:700}
.avatar{width:26px;height:26px;border-radius:50%;background:#8a96a3}
.news-card .foot{position:absolute;left:14px;top:355px;font-size:9.5px}

.site-footer{position:absolute;left:0;top:4111px;width:1200px;height:417px;background:linear-gradient(160deg,#3b88d2,#2f79c6)}
.site-footer .brand{position:absolute;left:155px;top:118px;font-size:44px;color:var(--white);letter-spacing:3px}
.site-footer .brand .dot{width:30px;height:30px;background:var(--white)}
.site-footer .tag{position:absolute;left:151px;top:232px;font-size:14px;line-height:22px;color:var(--white)}
.social{position:absolute;top:4404px;width:30px;height:30px;border-radius:50%;background:var(--white)}
.fcol h4{position:absolute;top:4254px;font-size:15px;font-weight:500;color:var(--white)}
.fcol a{position:absolute;font-size:10px;color:#e4eefa}
.legal{position:absolute;top:4494px;font-size:10px;color:#e4eefa}
</style>
</head>
<body>

<header class="site-header">
  <div class="brand"><span class="dot"></span>Velmora DX</div>
  <nav class="nav">
    <a style="left:492px" href="#">Home</a>
    <a style="left:571px" href="#">About Us</a>
    <a style="left:668px" href="#">Services</a>
    <a style="left:759px" href="#">News</a>
  </nav>
  <a class="btn contact-btn" href="#">CONTACT US</a>
</header>

<section class="hero">
  <h1>LIGHTING THE</h1>
  <div class="sub" style="top:270px">WAY TO EARLY CANCER</div>
  <div class="sub" style="top:343px">DETECTION</div>
  <div class="ux-label">USER<br>EXPERIENCE</div>
  <div class="play" style="left:1011px;top:418px"><svg width="12" height="12" viewBox="0 0 12 12"><path d="M3 1l8 5-8 5z" fill="var(--blue)"/></svg></div>
  <div class="photo" role="img" aria-label="Scientists working with microscopes in a laboratory" style="left:838px;top:480px;width:213px;height:128px;border-radius:6px;background:linear-gradient(135deg,#cfe3f5,#7aa9d6)"></div>
  <span class="hero-dot"></span>
  <div class="hero-note">Highlight Non-Invasive,<br>Urine-Based Diagnostics</div>
  <a class="btn" href="#" style="left:400px;top:566px;width:187px;height:42px">REQUEST ONBOARDING</a>
</section>

<h2 class="section-title" style="top:835px">OUR EDGE IN EARLY CANCER DETECTION</h2>

<div class="edge-card" style="left:151px">
  <svg width="100" height="100" viewBox="0 0 100 100"><circle cx="50" cy="50" r="44" fill="var(--blue-light)"/><rect x="44" y="34" width="12" height="30" rx="3" fill="var(--ink)"/></svg>
  <p>Non-Invasive,<br>Painless</p>
</div>
<div class="edge-card" style="left:380px">
  <svg width="100" height="100" viewBox="0 0 100 100"><circle cx="50" cy="50" r="44" fill="var(--blue-light)"/><path d="M38 50l8 8 16-16" stroke="var(--ink)" stroke-width="4" fill="none"/></svg>
  <p>Precision<br>Biomarkers</p>
</div>
<div class="edge-card active" style="left:608px">
  <svg width="100" height="100" viewBox="0 0 100 100"><circle cx="50" cy="50" r="44" fill="var(--ink)"/><g fill="var(--blue-light)"><circle cx="50" cy="50" r="5"/><circle cx="38" cy="40" r="4"/><circle cx="62" cy="40" r="4"/><circle cx="38" cy="60" r="4"/><circle cx="62" cy="60" r="4"/></g></svg>
  <p>AI-Powered<br>Insights</p>
</div>
<div class="edge-card" style="left:838px">
  <svg width="100" height="100" viewBox="0 0 100 100"><circle cx="50" cy="50" r="44" fill="var(--blue-light)"/><circle cx="48" cy="44" r="9" fill="var(--ink)"/><rect x="36" y="56" width="28" height="10" rx="5" fill="var(--ink)"/></svg>
  <p>Clinically Validated</p>
</div>

<section class="about">
  <div class="photo" role="img" aria-label="Sample cup held in a gloved hand, with a play button and caption" style="left:297px;top:1334px;width:283px;height:284px;border-radius:12px;background:linear-gradient(160deg,#a8cce9,#2f6fb3)"></div>
  <div class="play" style="left:309px;top:1563px;width:38px;height:38px"><svg width="13" height="13" viewBox="0 0 12 12"><path d="M3 1l8 5-8 5z" fill="var(--blue)"/></svg></div>
  <div class="abs" style="left:358px;top:1566px;font-size:15px;line-height:21px;color:var(--white);font-weight:500">Experience. Passion.<br>Craftsmanship</div>
  <div class="photo" role="img" aria-label="Researcher looking through a microscope" style="left:149px;top:1221px;width:283px;height:285px;border-radius:12px;border:5px solid var(--white);background:linear-gradient(135deg,#e4eef7,#7ea8d2)"></div>
  <div class="badge" style="left:402px;top:1258px;width:52px;height:52px"></div>
  <h2 style="top:1263px">OUR EDGE IN EARLY CANCER<br>DETECTION</h2>
  <p style="top:1383px">At Brightwell Construction, we're dedicated to delivering exceptional residential and commercial remodeling services that exceed our clients' expectations.</p>
  <p style="top:1453px">At Brightwell Construction, we're dedicated to delivering exceptional residential and commercial remodeling services that exceed our clients' expectations.</p>
  <a class="btn" href="#" style="left:610px;top:1530px;width:126px;height:44px">LEARN MORE</a>
</section>

<section class="test" role="img" aria-label="Blue-toned photograph of a scientist working at a microscope">
  <h2>A SIMPLE TEST FOR A SERIOUS DISEASE</h2>
  <div class="item" style="top:167px"><b>1)</b>Indication: high-risk individuals (familial history, pancreatitis, genetic risk).</div>
  <div class="note" style="top:200px">At Brightwell Construction, we're dedicated to delivering exceptional residential and</div>
  <div class="item" style="top:236px"><b>2)</b>Clinical output: Elevated vs Average risk</div>
  <div class="note" style="top:269px">At Brightwell Construction, we're dedicated to delivering exceptional residential and</div>
  <div class="item" style="top:305px"><b>3)</b>Indication: high-risk individuals (familial history, pancreatitis, genetic risk).</div>
  <div class="note" style="top:338px">At Brightwell Construction, we're dedicated to delivering exceptional residential and</div>
  <div class="item" style="top:373px"><b>4)</b>Target customers: Public health, private hospitals, labs, pharma</div>
  <div class="note" style="top:406px">At Brightwell Construction, we're dedicated to delivering exceptional residential and</div>
  <a class="btn" href="#" style="left:151px;top:447px;width:127px;height:43px">LEARN MORE</a>
</section>

<h2 class="section-title" style="top:2384px">TRUSTED DIAGNOSTICS BACKED BY CLINICAL EVIDENCE</h2>

<div class="evidence-card" style="left:153px">
  <div class="photo" role="img" aria-label="Patient at an eye examination device" style="background:linear-gradient(135deg,#f1e3d8,#9fb3c4)"></div>
  <div class="badge"></div>
  <h3>PARTNERS &amp;<br>COLLABORATIONS</h3>
  <p class="desc">Lorem Ipsum Dolor Sit Amet Consectetur. Mattis Libero Pellentesque Nisi Augue. Tortor</p>
  <div class="more">Mehr Lesen →</div>
</div>
<div class="evidence-card" style="left:380px">
  <div class="photo" role="img" aria-label="Illustration of a DNA double helix in blue and pink" style="background:linear-gradient(135deg,#1f64b7,#9ab5e3)"></div>
  <div class="badge"></div>
  <h3>CLINICAL<br>EVIDENC</h3>
  <p class="desc">Lorem Ipsum Dolor Sit Amet Consectetur. Mattis Libero Pellentesque Nisi Augue. Tortor</p>
  <div class="more">Mehr Lesen →</div>
</div>
<div class="evidence-card active" style="left:608px">
  <div class="photo" role="img" aria-label="Two researchers working with lab glassware" style="background:linear-gradient(135deg,#eef4f9,#a9c2d9)"></div>
  <div class="badge"></div>
  <h3>PARTNERS &amp;<br>COLLABORATIONS</h3>
  <p class="desc">Lorem Ipsum Dolor Sit Amet Consectetur. Mattis Libero Pellentesque Nisi Augue. Tortor</p>
  <div class="more">Mehr Lesen →</div>
</div>
<div class="evidence-card" style="left:836px">
  <div class="photo" role="img" aria-label="Laptop showing data charts" style="background:linear-gradient(135deg,#3e4a57,#b9c4cf)"></div>
  <div class="badge"></div>
  <h3>TECHNOLOGY<br>PLATFORM</h3>
  <p class="desc">Lorem Ipsum Dolor Sit Amet Consectetur. Mattis Libero Pellentesque Nisi Augue. Tortor</p>
  <div class="more">Mehr Lesen →</div>
</div>

<a class="btn" href="#" style="left:525px;top:2871px;width:150px;height:44px">DISCOVER MORE</a>

<section class="clarity">
  <h2>CLARITY ON WHAT MATTERS<br>MOST</h2>
  <div class="acc open" style="top:3126px;height:58px">Lorem Ipsum Dolor Sit Amet Consectetur.<span>−</span></div>
  <div class="acc-body">Lorem Ipsum Dolor Sit Amet Consectetur. Tellus Sociis Enim Sagittis Scelerisque Elit Pulvinar Eget. Odio Purus Rutrum Nam Eros Egestas Sit. Elementu Vulputate Ullamcorper Quis Elit. Quam Vitae Integer Quis Tortor Aliquam Aliquet.</div>
  <div class="acc" style="top:3321px;height:58px">Lorem Ipsum Dolor Sit Amet Consectetur.<span>+</span></div>
  <div class="acc" style="top:3391px;height:58px">Lorem Ipsum Dolor Sit Amet Consectetur.<span>+</span></div>
  <div class="photo" role="img" aria-label="Empty modern laboratory in blue light" style="left:611px;top:3011px;width:440px;height:436px;border-radius:14px;background:linear-gradient(160deg,#8ec3ee,#2f72c2 60%,#1c4f96)"></div>
</section>

<h2 class="section-title" style="top:3548px">THOUGHTS, NEWS, AND SCIENTIFIC BREAKTHROUGHS</h2>

<article class="news-card" style="left:149px">
  <div class="photo" role="img" aria-label="Researcher in protective gear handling samples" style="background:linear-gradient(135deg,#1e5fa8,#8ec6ee)"></div>
  <h3>PARTNERS &amp; COLLABORATIONS</h3>
  <p class="lead">For A Sleek, Low-Maintenance Option, Our Powder.</p>
  <hr>
  <div class="author"><span class="avatar"></span>Mara Ellison</div>
  <p class="foot">For A Sleek, Low-Maintenance Option, Our Powder.</p>
</article>
<article class="news-card" style="left:453px">
  <div class="photo" role="img" aria-label="Scientist viewing a holographic data display" style="background:linear-gradient(135deg,#163f6b,#3aa0b8)"></div>
  <h3>CLINICAL EVIDENC</h3>
  <p class="lead">For A Sleek, Low-Maintenance Option, Our Powder.</p>
  <hr>
  <div class="author"><span class="avatar"></span>Mara Ellison</div>
  <p class="foot">For A Sleek, Low-Maintenance Option, Our Powder.</p>
</article>
<article class="news-card" style="left:759px">
  <div class="photo" role="img" aria-label="Researcher in protective suit beside virus illustrations" style="background:linear-gradient(135deg,#d8e6f2,#2d6fb5)"></div>
  <h3>TECHNOLOGY PLATFORM</h3>
  <p class="lead">For A Sleek, Low-Maintenance Option, Our Powder.</p>
  <hr>
  <div class="author"><span class="avatar"></span>Mara Ellison</div>
  <p class="foot">For A Sleek, Low-Maintenance Option, Our Powder.</p>
</article>

<footer class="site-footer">
  <div class="brand"><span class="dot"></span>Velmora DX</div>
  <p class="tag">Lorem Ipsum Dolor Amet Consectetur. Mauris Enim<br>Dapibus Mauris Leo</p>
</footer>
<span class="social" style="left:152px" aria-label="Social link"></span>
<span class="social" style="left:201px" aria-label="Social link"></span>
<span class="social" style="left:252px" aria-label="Social link"></span>
<span class="social" style="left:303px" aria-label="Social link"></span>
<div class="fcol">
  <h4 style="left:806px">Menu</h4>
  <a style="left:806px;top:4295px" href="#">Home</a>
  <a style="left:806px;top:4323px" href="#">About</a>
  <a style="left:806px;top:4351px" href="#">Services</a>
  <a style="left:806px;top:4379px" href="#">News</a>
  <a style="left:806px;top:4407px" href="#">Contact</a>
  <h4 style="left:921px">Contact Us</h4>
  <a style="left:921px;top:4295px" href="#">✆ (555) 014-2290</a>
  <a style="left:921px;top:4323px" href="#">✉ hello@velmoradx.example</a>
  <a style="left:921px;top:4351px;line-height:15px" href="#">⌖ 48 Harlow Court,<br>&nbsp;&nbsp;&nbsp;Dunmere, DM</a>
</div>
<div class="legal" style="left:151px">Copyright © 2025 Velmora DX</div>
<div class="legal" style="left:866px">Privacy Policy</div>
<div class="legal" style="left:958px">Term and conditions</div>

</body>
</html>
```